Capability Statement Flyer

We want to develop a flyer to show potential clients our work capability. We want to incorporate our logo. You can reference our website for any other graphics you may want to incorporate. Our blue CMYK is 100-80-0-22

Colors
0555a3

Requirements
Must have
• Capability Statement
• Our expertise and technical resources fuel the delivery of our services. As a leading provider of construction services, Halvern Construction focuses on providing solutions for civil infrastructure, industrial infrastructure, and commercial market segments. Driven by a commitment to continuous improvement, Halvern Construction has the expertise in the following key areas:
• • Design Build/Problem Solving
• • Storm and Process Water Systems
• • Heavy and Structural Concrete
• • Bridge Construction
• • Building Construction and Restoration
• • Hardscapes
• • All Civil Construction and Utility
Nice to have
• Creativity to present to potential clients. Not just words on the page

```html
<!DOCTYPE html>
<html lang="en">
<head>
<meta charset="utf-8">
<title>Halvern Construction – Capability Statement</title>
<link rel="stylesheet" href="https://fonts.googleapis.com/css2?family=Roboto:wght@300&family=Roboto+Condensed:wght@700&family=Open+Sans:wght@400;700&display=swap">
<style>
:root{
  --brand-blue:#0555a3;
  --navy:#25398a;
  --ink:#1b1b1b;
  --paper:#f3f3f5;
  --footer:#333335;
  --backdrop:#8a8a8a;
}
*{margin:0;padding:0;box-sizing:border-box}
html,body{width:1200px;height:1072px;overflow:hidden;background:var(--backdrop)}
.flyer{position:absolute;left:221px;top:0;width:757px;height:1072px;background:var(--paper);overflow:hidden;font-family:"Open Sans",sans-serif;color:var(--ink)}
.hero{position:absolute;left:0;top:0}
.brand{position:absolute;top:382px;left:0;width:757px;display:flex;justify-content:center;align-items:center;gap:10px}
.brand-square{width:58px;height:58px;background:var(--navy)}
.brand-name{font-family:"Roboto Condensed",sans-serif;font-weight:700;font-size:44px;line-height:1;color:var(--navy);letter-spacing:.5px}
.tagline{position:absolute;top:466px;width:100%;text-align:center;font-family:"Roboto",sans-serif;font-weight:300;font-size:33px;color:#111}
.headline{position:absolute;top:506px;width:100%;text-align:center;font-family:"Roboto Condensed",sans-serif;font-weight:700;font-size:46px;color:var(--navy);letter-spacing:.5px}
.areas{position:absolute;left:57px;top:622px;width:645px;height:229px;border:1.5px solid #222;border-radius:14px}
.areas-title{position:absolute;top:584px;width:100%;text-align:center;font-weight:700;font-size:19px;line-height:25px;color:#1b1b1b;z-index:2}
.areas-title .gap{background:var(--paper);padding:0 8px}
.area{position:absolute;text-align:center;font-size:11px;color:#222;transform:translateX(-50%);white-space:nowrap}
.area svg{display:block;margin:0 auto 6px}
.cap-bar{position:absolute;left:53px;top:877px;width:648px;height:44px;background:var(--brand-blue);color:#fff;font-weight:700;font-size:23px;text-align:center;line-height:44px}
.cap-bar::after{content:"";position:absolute;left:331px;bottom:-15px;border-left:15px solid transparent;border-right:15px solid transparent;border-top:15px solid var(--brand-blue)}
.cap-text{position:absolute;left:53px;top:954px;width:648px;font-size:11.3px;line-height:14px;text-align:justify;color:#222}
.footer{position:absolute;left:0;top:1013px;width:757px;height:45px;background:var(--footer);color:#fff;font-size:10.5px}
.footer-item{position:absolute;top:0;height:45px;display:flex;align-items:center;gap:10px}
.footer-rule{position:absolute;left:0;top:1061px;width:757px;height:11px;background:#0c0c0c}
</style>
</head>
<body>
<main class="flyer">
  <svg class="hero" width="757" height="460" viewBox="0 0 757 460">
    <defs>
      <linearGradient id="site" x1="0" y1="0" x2="1" y2="1">
        <stop offset="0" stop-color="#9cc3e4"/>
        <stop offset=".4" stop-color="#a88f78"/>
        <stop offset=".75" stop-color="#d9692f"/>
        <stop offset="1" stop-color="#4a4a4a"/>
      </linearGradient>
    </defs>
    <polygon role="img" aria-label="Photo of two engineers in hard hats and safety vests reviewing plans at a building site" points="0,0 757,0 757,245 688,338 72,338 0,442" fill="url(#site)"/>
    <polyline points="757,252 691,346 76,346 0,452" fill="none" stroke="var(--brand-blue)" stroke-width="10"/>
  </svg>

  <div class="brand"><div class="brand-square"></div><div class="brand-name">HALVERN CONSTRUCTION</div></div>

  <p class="tagline">Quality construction • Innovative solutions</p>
  <h1 class="headline">FIRST CLASS DELIVERY</h1>

  <section class="areas">
    <div class="area" style="left:99px;top:38px">
      <svg width="34" height="42" viewBox="0 0 34 42" fill="none" stroke="#222" stroke-width="2"><path d="M2 42V26h6v16M12 42V12h6v30M22 42V2M22 20h8v22"/></svg>Design Build/Problem Solving</div>
    <div class="area" style="left:313px;top:38px">
      <svg width="40" height="42" viewBox="0 0 40 42"><path d="M20 2 2 18h5v12h26V18h5z" fill="#222"/><rect x="16" y="20" width="8" height="10" fill="#fff"/><path d="M2 34q5-4 9 0t9 0 9 0 9 0M2 40q5-4 9 0t9 0 9 0 9 0" stroke="#222" stroke-width="2.5" fill="none"/></svg>Storm and Process Water Systems</div>
    <div class="area" style="left:526px;top:38px">
      <svg width="44" height="42" viewBox="0 0 44 42" fill="none" stroke="#222" stroke-width="2.5"><circle cx="22" cy="21" r="12"/><path d="M22 13v8h7"/><path d="M6 14a17 17 0 0 1 10-10M38 28a17 17 0 0 1-10 10M28 4a17 17 0 0 1 10 10M16 38A17 17 0 0 1 6 28"/></svg>Building Construction and Restoration</div>
    <div class="area" style="left:101px;top:130px">
      <svg width="40" height="30" viewBox="0 0 40 30"><rect x="2" y="10" width="12" height="12" fill="#222"/><path d="M16 6h16l6 10v6H16z" fill="#222"/><circle cx="9" cy="25" r="4" fill="#222" stroke="#fff" stroke-width="1.5"/><circle cx="24" cy="25" r="4" fill="#222" stroke="#fff" stroke-width="1.5"/><circle cx="33" cy="25" r="4" fill="#222" stroke="#fff" stroke-width="1.5"/></svg>Heavy and Structural Concrete</div>
    <div class="area" style="left:254px;top:130px">
      <svg width="56" height="32" viewBox="0 0 56 32"><path d="M2 30q26-22 52 0z" fill="#222"/><circle cx="28" cy="10" r="6" fill="#222"/><rect x="27" y="12" width="2" height="8" fill="#222"/></svg>Hardscapes</div>
    <div class="area" style="left:375px;top:130px">
      <svg width="60" height="30" viewBox="0 0 60 30" fill="none" stroke="#222" stroke-width="2.5"><path d="M2 20h56M15 6v22M45 6v22M2 14q13-10 13-8 0 2 15 14 15-12 15-14 0-2 13 8"/></svg>Bridge Construction</div>
    <div class="area" style="left:542px;top:130px">
      <svg width="40" height="32" viewBox="0 0 40 32"><path d="M4 18l14-6 18 6v10l-18 4-14-6z" fill="#222"/><path d="M20 14 34 2" stroke="#222" stroke-width="3"/><path d="M12 12l10-4 4 4-10 4z" fill="#222"/></svg>All Civil Construction and Utility</div>
  </section>

  <h2 class="areas-title">HALVERN CONSTRUCTION<br><span class="gap">has the expertise in the following key areas</span></h2>

  <h2 class="cap-bar">CAPABILITY STATEMENT</h2>
  <p class="cap-text">Our expertise and technical resources fuel the delivery of our services. As a leading provider of construction services, Halvern Construction&nbsp; focuses on providing solutions for civil infrastructure, industrial infrastructure, and commercial market&nbsp; segments. Driven by a commitment to continuous improvement,</p>

  <footer class="footer">
    <div class="footer-item" style="left:55px"><svg width="10" height="13" viewBox="0 0 10 13"><path d="M5 12S1 7 1 5a4 4 0 0 1 8 0c0 2-4 7-4 7z" fill="none" stroke="#fff" stroke-width="1.3"/><circle cx="5" cy="5" r="1.5" fill="#fff"/></svg>2210 Foundry Park Road Millbrook, Ohio 44021</div>
    <div class="footer-item" style="left:392px"><svg width="12" height="12" viewBox="0 0 12 12"><path d="M2 1l3 3-1.5 1.5a7 7 0 0 0 3 3L8 7l3 3-2 2C5 12 0 7 0 3z" fill="#fff"/></svg>555.014.2225</div>
    <div class="footer-item" style="left:552px;gap:34px"><svg width="16" height="14" viewBox="0 0 16 14"><rect x="0" y="3" width="4" height="11" fill="#fff"/><rect x="5" y="5" width="11" height="9" fill="#fff"/><rect x="7" y="0" width="7" height="5" fill="none" stroke="#fff"/></svg>555.014.2202/ 555.019.4374</div>
  </footer>
  <div class="footer-rule"></div>
</main>
</body>
</html>
```